バリエーション多く提案していただき採用させていただきました。
自分の意図している事を非常に再現性高く提案していただきありがとうございます。
ご応募いただきありがとうございます。今後も募集しますので何卒宜しくお願いします。
恋愛学習コンテンツの動画サムネイル バナー作成の仕事の依頼
女性的 男性的
希望する色 特になし・その他 追記事項: カテゴリごとに色変えてほしい
特記事項
• 継続依頼あり
• 参考記事URL
https://palvento-mirai.example/korunade

```html
<!DOCTYPE html>
<html lang="ja">
<head>
<meta charset="utf-8">
<title>会話の際にこの人いいなと思わせる方法3選 会話編</title>
<link href="https://fonts.googleapis.com/css2?family=Noto+Sans+JP:wght@700;900&display=swap" rel="stylesheet">
<style>
  :root {
    --bg: #050505;
    --ink: #ffffff;
    --accent-red: #e0141b;
    --band-green: #1f7a45;
    --band-ink: #0a0a0a;
    --photo-dark: #1a1a1a;
    --photo-mid: #4a4a4a;
    --photo-light: #bdbdbd;
  }
  html, body {
    margin: 0;
    padding: 0;
    width: 1200px;
    height: 676px;
    overflow: hidden;
    background: var(--bg);
  }
  .thumbnail {
    position: relative;
    width: 1200px;
    height: 676px;
    background: var(--bg);
    overflow: hidden;
    font-family: "Noto Sans JP", sans-serif;
    color: var(--ink);
  }
  .portrait {
    position: absolute;
    left: 0;
    top: 0;
    width: 680px;
    height: 676px;
    background:
      radial-gradient(ellipse 60% 80% at 30% 45%, var(--photo-mid) 0%, var(--photo-dark) 55%, transparent 80%),
      linear-gradient(90deg, var(--photo-dark) 0%, #2a2a2a 50%, transparent 100%);
    box-shadow: inset -30px 0 60px -40px var(--photo-light);
    border-radius: 0 45% 0 0 / 0 20% 0 0;
  }
  .headline {
    position: absolute;
    margin: 0;
    font-weight: 700;
    line-height: 1;
    white-space: nowrap;
  }
  .headline-lead {
    left: 684px;
    top: 30px;
    font-size: 94px;
  }
  .headline-key {
    left: 318px;
    top: 126px;
    font-size: 142px;
    font-weight: 900;
    letter-spacing: 2px;
  }
  .key-underline {
    position: absolute;
    left: 320px;
    top: 280px;
    width: 872px;
    height: 12px;
    background: var(--accent-red);
  }
  .headline-tail {
    left: 340px;
    top: 338px;
    font-size: 70px;
  }
  .count {
    position: absolute;
    left: 858px;
    top: 316px;
    font-weight: 900;
    line-height: 1;
    white-space: nowrap;
  }
  .count-number {
    display: inline-block;
    font-size: 170px;
    transform: skewX(-14deg);
  }
  .count-word {
    font-size: 160px;
  }
  .category-band {
    position: absolute;
    left: 0;
    top: 494px;
    width: 1200px;
    height: 138px;
  }
  .category-label {
    position: absolute;
    left: 610px;
    top: 512px;
    margin: 0;
    font-size: 100px;
    font-weight: 900;
    line-height: 1;
    color: var(--band-ink);
  }
</style>
</head>
<body>
  <main class="thumbnail">
    <div class="portrait" role="img" aria-label="スーツ姿の男性のモノクロ写真（首から下、ジャケットの前を整える手元）"></div>

    <p class="headline headline-lead">会話の際に</p>
    <h1 class="headline headline-key">この人いいな</h1>
    <div class="key-underline"></div>
    <p class="headline headline-tail">と思わせる方法</p>
    <p class="count"><span class="count-number">3</span><span class="count-word">選</span></p>

    <svg class="category-band" viewBox="0 0 1200 138" aria-hidden="true">
      <polygon points="560,0 1200,0 1200,138 490,138" fill="var(--band-green)"/>
    </svg>
    <p class="category-label">会話編</p>
  </main>
</body>
</html>
```